Brambleton Resource Holdings, LP Letter Head

We need an official company letter head design that is clean and mimics our company logo style. It will include our logo, address, phone, and website. We are an OIl and Gas mineral purchasing company, so hints of oil rigs or related design would be desirable.

Industry/Entity Type

Oil And Gas

Colors
ec1f27
f04a50
f59195
fbd4d5

Requirements
Must have
• Logo
• 7392 Whitcombe R. Ashdale Parkway, Suite 618
• Dallas TX, 75391
• 214-673-1958
• www.bramblestoneres.example
Nice to have
• Oil Rigs or OIl and gas related design

```html
<!DOCTYPE html>
<html lang="en">
<head>
<meta charset="utf-8">
<title>Brambleton Resource Holdings – Letterhead</title>
<link rel="stylesheet" href="https://fonts.googleapis.com/css2?family=Cinzel:wght@500&family=Questrial&display=swap">
<style>
  :root {
    --red: #ec1f27;
    --red-deep: #c8141c;
    --red-mid: #f04a50;
    --red-soft: #f59195;
    --red-pale: #fbd4d5;
    --ink: #2b2b2b;
    --paper: #ffffff;
    --backdrop: #dccfb6;
  }
  * { box-sizing: border-box; margin: 0; padding: 0; }
  html, body { width: 1200px; height: 893px; overflow: hidden; }
  body { background: var(--backdrop); font-family: "Questrial", sans-serif; color: var(--ink); }

  .letterhead {
    position: absolute; left: 300px; top: 22px;
    width: 600px; height: 849px;
    background: var(--paper);
    box-shadow: 0 6px 24px rgba(0,0,0,.18);
    overflow: hidden;
  }
  .brand-column {
    position: absolute; left: 44px; top: 0;
    width: 74px; height: 170px;
    background: var(--red);
  }
  .brand-name {
    position: absolute; left: 140px; top: 46px;
    font-family: "Cinzel", serif; font-weight: 500;
    color: var(--red-deep); line-height: 1;
  }
  .brand-name .primary { display: block; font-size: 36px; letter-spacing: .5px; }
  .brand-name .secondary { display: block; font-size: 14px; letter-spacing: 5px; margin-top: 6px; }

  .oilfield-art {
    position: absolute; left: 0; right: 0; top: 570px; height: 139px;
    background: linear-gradient(to bottom, rgba(251,212,213,0) 0%, rgba(251,212,213,.7) 100%);
  }

  .letter-body {
    position: absolute; left: 70px; top: 240px; width: 450px;
    font-size: 11px; line-height: 1.75; color: #333;
  }
  .letter-body p + p { margin-top: 22px; }

  .signature {
    position: absolute; left: 430px; top: 628px;
  }
  .signature .name { font-size: 14px; color: var(--ink); }
  .signature .title { font-size: 9px; color: #555; margin-top: 3px; }

  .footer-band {
    position: absolute; left: 0; right: 0; bottom: 0; height: 140px;
    background: var(--red-deep);
    color: var(--red-pale);
    font-size: 11.5px; letter-spacing: .3px;
    padding: 32px 0 0 56px;
  }
  .footer-band .contact-line { display: flex; gap: 22px; }
  .footer-band .address { margin-top: 10px; }
</style>
</head>
<body>
  <main class="letterhead">
    <div class="brand-column"></div>
    <div class="brand-name">
      <span class="primary">Brambleton</span>
      <span class="secondary">Resource Holdings, LP</span>
    </div>

    <div class="oilfield-art" role="img" aria-label="Faint pink silhouettes of oil derricks and pump jacks along the lower edge"></div>

    <section class="letter-body">
      <p>Lorem ipsum dolor sit amet, consectetur adipiscing elit. Donec orci purus, luctus vitae dignissim eu, iaculis sed purus. Vivamus faucibus, ipsum nec aliquet viverra, leo mauris condimentum ligula, sit amet sagittis enim ligula quis arcu. Nam egestas tortor id nisi porttitor mattis. In tortor ante, ultricies in suscipit a, tempus non massa. Vivamus et auctor mi. Fusce vel massa nulla. Phasellus nec eros mauris, et scelerisque orci. Donec malesuada orci vitae nulla accumsan porta a id massa. Quisque accumsan iaculis magna sit amet fringilla. Maecenas consequat, magna eget tincidunt semper, odio nibh rutrum mi, id feugiat ante nisi eu risus. Vestibulum nunc orci, rhoncus a placerat in, ultricies in mi. Cras mattis varius eros, vel fringilla nisl suscipit eget.</p>
      <p>Quisque scelerisque sagittis nulla at porttitor. Mauris a justo et tellus interdum tristique. Sed id augue vitae urna euismod commodo aliquet a quam. Pellentesque arcu velit, cursus et malesuada ut, consequat et diam. Nullam erat sem, rhoncus id ullamcorper vitae, rhoncus et arcu. In ultricies ultricies nulla, ut rutrum nisl iaculis at. Donec eu magna a metus ornare faucibus. Fusce aliquet faucibus ultricies. Morbi semper, est id tincidunt gravida, sem arcu adipiscing lacus, ac bibendum nulla leo eu purus. Quisque nec diam sed risus consectetur a accumsan quis quis nibh. Vestibulum id purus lorem.</p>
    </section>

    <div class="signature">
      <div class="name">Daniel Whitford</div>
      <div class="title">Co-Founder &amp; CEO</div>
    </div>

    <footer class="footer-band">
      <div class="contact-line">
        <span>214-673-1958</span>
        <span>www.bramblestoneres.example</span>
      </div>
      <div class="address">7392 Whitcombe R. Ashdale Parkway, Suite 618 Dallas TX, 75391</div>
    </footer>
  </main>
</body>
</html>
```